Revamping MarcelTovrin.com like a portal of all services

I have my website marceltovrin.com that is about my trading school.
I have pipmasterhub.com for my currencies strategies,
I have mt-vault.com for my crypto strategy.

I would like to regroup all under marceltovrin.com by revamping all this website in one brand new

1-Color code under mt-vault.com
2-All my 3 services on different one pager connected to the home page.
3-Need attractive website. Any disruptive feature is welcome.

The website should be a portal resuming all the activities of Marcel Tovrin as described below:

Page 1 :
Home Page presenting the 3 services of marcel tovrin

Page 2 :
One pager presenting https://pipmasterhub.com

Page 3:
One pager presenting https://mt-vault.com

Page 4:
One pager presenting https://marceltovrin.com/bluepath/

Page 5:
Page for faq and contact

Target Market(s)

Financial investors

Industry/Entity Type

Finance Crypto

Coding

Coded - Design and coding required

Number of Pages Required

5+ page

Requirements
Must have
• Financial elements
Nice to have
• Animated element

```html
<!DOCTYPE html>
<html lang="en">
<head>
<meta charset="utf-8">
<title>Marcel Tovrin – Trading Coach</title>
<link href="https://fonts.googleapis.com/css2?family=Roboto:wght@400;500;700;900&display=swap" rel="stylesheet">
<style>
:root{
  --purple:#8a1fc7;
  --pink:#f451c0;
  --grad:linear-gradient(90deg,var(--purple),var(--pink));
  --ink:#222;
  --text:#666;
  --light:#f2f2f2;
  --field:#f4f4f4;
  --footer:#222222;
  --green:#3ab54a;
  --blue:#2b3fd6;
}
*{box-sizing:border-box;margin:0;padding:0}
html,body{width:1200px;height:2952px;overflow:hidden}
body{position:relative;font-family:'Roboto',sans-serif;color:var(--ink);background:#fff}
.abs{position:absolute}

/* header */
.site-header{left:0;top:0;width:1200px;height:101px;background:#fff}
.brand{left:111px;top:10px;width:130px;display:flex;flex-direction:column;align-items:center}
.brand-mark{width:30px;height:30px;border-radius:50%;background:var(--blue);margin-bottom:4px}
.brand-name{font-size:19px;font-weight:500;color:var(--blue);line-height:1}
.brand-tag{font-size:11px;color:var(--green);margin-top:3px}
.main-nav{left:314px;top:41px;display:flex;gap:25px;font-size:14px;font-weight:700}
.main-nav a{color:var(--ink);text-decoration:none;position:relative}
.main-nav a.active{color:#d640b5}
.main-nav a.active::before{content:"";position:absolute;left:0;right:0;top:-41px;height:3px;background:#d640b5}
.social{display:flex;gap:5px}
.social span{width:37px;height:37px;border-radius:50%;background:#fff;box-shadow:0 2px 8px rgba(0,0,0,.18);display:block}
.social span:first-child{background:var(--grad)}
.header-social{left:886px;top:32px}

/* hero */
.hero{left:0;top:101px;width:1200px;height:598px;background:linear-gradient(100deg,#7a1eb8 0%,#a42bc4 45%,#e048c0 75%,#f565c8 100%)}
.hero-portrait{left:625px;top:60px;width:424px;height:538px;background:linear-gradient(180deg,#c64bb5 0%,#2a2f6e 45%,#1d2560 100%);border-radius:200px 200px 0 0;opacity:.9}
.hero-title{left:110px;top:214px;font-size:47px;font-weight:900;color:#fff;letter-spacing:.5px}
.hero-sub{left:111px;top:279px;font-size:21px;font-weight:500;color:#fff}
.signup{left:111px;top:329px;width:514px;height:50px;background:#fff;border-radius:4px;display:flex;align-items:center;padding:3px}
.signup .field{flex:1;padding-left:14px;font-size:16px;color:#333}
.signup .btn{width:125px;height:44px;background:var(--grad);color:#fff;font-weight:700;font-size:15px;display:flex;align-items:center;justify-content:center;border-radius:3px}
.dots{left:111px;top:560px;display:flex;gap:7px}
.dots span{width:13px;height:13px;border:2px solid #fff;border-radius:50%}
.dots span.on{background:#fff}

/* about */
.about{left:0;top:699px;width:1200px;height:521px;background:var(--light)}
.about-frame{left:111px;top:72px;width:462px;height:358px;border:6px solid var(--purple);border-right:none;border-radius:14px 0 0 14px}
.about-frame::after{content:"";position:absolute;top:-6px;left:0;width:462px;height:6px;background:var(--grad);border-radius:0 10px 0 0}
.about-photo{left:128px;top:89px;width:462px;height:358px;background:#fff;border-radius:10px;padding:8px;box-shadow:0 2px 10px rgba(0,0,0,.1)}
.about-photo div{width:100%;height:100%;border-radius:6px;background:linear-gradient(160deg,#d9d9d6,#a9a9a3 60%,#8c8a85)}
.about-title{left:654px;top:130px;font-size:25px;font-weight:700;letter-spacing:.5px}
.about-text{left:654px;top:188px;width:435px;font-size:15.5px;line-height:26.7px;color:var(--text);text-align:justify}
.btn-grad{background:var(--grad);color:#fff;font-weight:700;font-size:15px;display:flex;align-items:center;justify-content:center;border-radius:4px}
.about-btn{left:654px;top:353px;width:129px;height:50px}

/* services */
.section-title{width:1200px;left:0;text-align:center;font-size:33px;font-weight:900;letter-spacing:.5px}
.services-title{top:1332px}
.card{top:1399px;width:311px;height:378px;background:#fff;box-shadow:0 2px 10px rgba(0,0,0,.12);border-radius:4px;text-align:center;padding:7px}
.card-img{width:297px;height:194px}
.card h3{font-size:19px;font-weight:700;margin-top:22px}
.card p{font-size:13.5px;line-height:24.5px;color:var(--text);margin:10px 8px 0}
.card .more{font-size:14px;font-weight:700;color:#b02cc2;margin-top:10px;display:flex;justify-content:center;align-items:center;gap:6px}
.card .more svg{width:14px;height:14px}
.arrow{top:1570px;width:37px;height:37px;border-radius:50%;display:flex;align-items:center;justify-content:center}
.arrow-prev{left:40px;border:2px solid #b02cc2;background:#fff}
.arrow-next{left:1123px;background:var(--grad)}

/* programme */
.programme{left:0;top:1867px;width:1200px;height:320px;background:linear-gradient(100deg,#8a22c8 0%,#b832c6 45%,#e44cc3 75%,#f86ccc 100%);text-align:center;color:#fff}
.programme h2{font-size:33px;font-weight:900;margin-top:45px;letter-spacing:.5px}
.programme p{font-size:16.5px;line-height:26.5px;width:900px;margin:22px auto 0}
.programme .btn-white{position:absolute;left:527px;top:216px;width:146px;height:50px;background:#fff;border-radius:4px;font-weight:700;font-size:15px;color:#b02cc2;display:flex;align-items:center;justify-content:center}

/* contact */
.contact-title{top:2262px}
.input{background:var(--field);border-radius:3px;box-shadow:0 3px 0 #ececec;font-size:14.5px;color:#666;padding:13px 15px}
.send-btn{left:523px;top:2535px;width:154px;height:50px}

/* footer */
.site-footer{left:0;top:2674px;width:1200px;height:278px;background:var(--footer);color:#fff}
.footer-brand{left:535px;top:22px;width:130px;display:flex;flex-direction:column;align-items:center}
.footer-brand .brand-mark{background:#fff;width:28px;height:28px}
.footer-brand .brand-name,.footer-brand .brand-tag{color:#fff}
.footer-nav{left:0;width:1200px;top:120px;display:flex;justify-content:center;gap:0;font-size:18px;font-weight:500}
.footer-nav span.sep{margin:0 24px}
.footer-social{left:500px;top:163px}
.footer-social span{background:transparent;border:2px solid #fff;box-shadow:none}
.footer-social span:first-child{border:none}
.footer-rule{left:111px;top:224px;width:978px;height:1px;background:#555}
.copyright{left:503px;top:240px;font-size:14px}
.legal{left:851px;top:240px;font-size:14px}
</style>
</head>
<body>

<header class="site-header abs">
  <div class="brand abs"><span class="brand-mark"></span><span class="brand-name">Marcel Tovrin</span><span class="brand-tag">Trading Coach</span></div>
  <nav class="main-nav abs">
    <a class="active">HOME</a><a>PIPMASTER HUB</a><a>MT-VAULT</a><a>BLUE PATH</a><a>FAQ</a><a>CONTACT</a>
  </nav>
  <div class="social header-social abs" aria-label="Social links"><span></span><span></span><span></span><span></span><span></span></div>
</header>

<section class="hero abs">
  <div class="hero-portrait abs" role="img" aria-label="Portrait of Marcel Tovrin in a navy shirt, smiling"></div>
  <h1 class="hero-title abs">MARCEL TOVRIN</h1>
  <p class="hero-sub abs">The world’s most popular Fx trader in social trading</p>
  <div class="signup abs"><span class="field">Email Address</span><span class="btn">JOIN NOW</span></div>
  <div class="dots abs"><span></span><span class="on"></span><span></span><span></span></div>
</section>

<section class="about abs">
  <div class="about-frame abs"></div>
  <div class="about-photo abs"><div role="img" aria-label="Trading desk with a wall screen showing market charts and a laptop"></div></div>
  <h2 class="about-title abs">ABOUT MARCEL TOVRIN</h2>
  <p class="about-text abs">Marcel Tovrin, world’s most popular Fx trader in social trading presents: The Blue Path : the best way to become a real trader. Learn and get all the tools to be a better trader, Improve your skills to be regular in your trading, detect opportunities on the markets with easy to replicate strategies.</p>
  <div class="btn-grad about-btn abs">READ MORE</div>
</section>

<h2 class="section-title services-title abs">OUR SERVICES</h2>
<div class="arrow arrow-prev abs"><svg width="12" height="12" viewBox="0 0 12 12"><path d="M8 1 3 6l5 5" fill="none" stroke="#333" stroke-width="2"/></svg></div>
<div class="arrow arrow-next abs"><svg width="12" height="12" viewBox="0 0 12 12"><path d="M4 1l5 5-5 5" fill="none" stroke="#fff" stroke-width="2"/></svg></div>

<article class="card abs" style="left:111px">
  <div class="card-img" role="img" aria-label="Student analysing charts on a desktop screen at night" style="background:linear-gradient(135deg,#1e3a5c,#4a3a2e 60%,#7a5a3c)"></div>
  <h3>PAST ANALYSIS</h3>
  <p>I am taking into consideration the personal history of each student so that I can adapt my teaching methods for you</p>
  <div class="more">READ MORE <svg viewBox="0 0 14 14"><circle cx="7" cy="7" r="7" fill="#b02cc2"/><path d="M4 7h5M7 4.5 9.5 7 7 9.5" stroke="#fff" stroke-width="1.6" fill="none"/></svg></div>
</article>
<article class="card abs" style="left:445px">
  <div class="card-img" role="img" aria-label="Coach pointing at a stock chart on a monitor beside a student" style="background:linear-gradient(135deg,#e9edf2,#c8ced6 60%,#9aa4b0)"></div>
  <h3>COACHING CLASSES</h3>
  <p>There will be weekly sessions from an upstream questionnaire and a ‘basics session’ with an explanation of the tools and methods.</p>
  <div class="more">READ MORE <svg viewBox="0 0 14 14"><circle cx="7" cy="7" r="7" fill="#b02cc2"/><path d="M4 7h5M7 4.5 9.5 7 7 9.5" stroke="#fff" stroke-width="1.6" fill="none"/></svg></div>
</article>
<article class="card abs" style="left:778px">
  <div class="card-img" role="img" aria-label="Trader typing on a laptop showing a market dashboard" style="background:linear-gradient(135deg,#8a6a4e,#c9b8a4 55%,#e6e2dc)"></div>
  <h3>TRADING DASHBOARD</h3>
  <p>You will have all the necessary tools to better understand the market movement and know how to detect opportunities.</p>
  <div class="more">READ MORE <svg viewBox="0 0 14 14"><circle cx="7" cy="7" r="7" fill="#b02cc2"/><path d="M4 7h5M7 4.5 9.5 7 7 9.5" stroke="#fff" stroke-width="1.6" fill="none"/></svg></div>
</article>

<section class="programme abs" role="img" aria-label="Programme banner over a tinted image of hands on a laptop with charts">
  <h2>OUR PROGRAMME</h2>
  <p>Empowered with 20 years of experience in the financial markets and my proven results over many years, I have decided to share my knowledge on how I became a consistent and profitable trader. A step by step programme to understand what matters and focus on the essential.</p>
  <div class="btn-white">SIGN UP NOW</div>
</section>

<h2 class="section-title contact-title abs">GET IN TOUCH</h2>
<div class="input abs" style="left:236px;top:2333px;width:359px;height:45px">First Name</div>
<div class="input abs" style="left:604px;top:2333px;width:360px;height:45px">Last Name</div>
<div class="input abs" style="left:236px;top:2386px;width:359px;height:45px">Phone</div>
<div class="input abs" style="left:604px;top:2386px;width:360px;height:45px">Email</div>
<div class="input abs" style="left:236px;top:2439px;width:728px;height:80px">Message</div>
<div class="btn-grad send-btn abs">SEND MESSAGE</div>

<footer class="site-footer abs">
  <div class="brand footer-brand abs"><span class="brand-mark"></span><span class="brand-name">Marcel Tovrin</span><span class="brand-tag">Trading Coach</span></div>
  <nav class="footer-nav abs"><span>HOME</span><span class="sep">|</span><span>PIPMASTER HUB</span><span class="sep">|</span><span>MT-VAULT</span><span class="sep">|</span><span>BLUE PATH</span><span class="sep">|</span><span>FAQ</span><span class="sep">|</span><span>CONTACT</span></nav>
  <div class="social footer-social abs" aria-label="Social links"><span></span><span></span><span></span><span></span><span></span></div>
  <div class="footer-rule abs"></div>
  <p class="copyright abs">Copyright © 2022 Marcel Tovrin</p>
  <p class="legal abs">Terms &amp; Conditons &nbsp;&nbsp;&nbsp;|&nbsp;&nbsp;&nbsp; Privacy Policy</p>
</footer>

</body>
</html>
```